Marlowe's Classic Dressing

We are looking for a new label as we switch or glass bottle from a traditional bottle to a round bottle. We want to create a newer/ more appealing logo, while still maintaining some of our old label features to ensure that the brand awareness is not lost. We like the coloring of the blue and white, but feel free to play around with other colors in the design.
We are looking to add product features to our label such as "Gluten-Free", "Original Recipe From 1957" "Family Owned". With this being an older company we would like to keep the traditional feel of our label with some added modern touches.
We are not married to the greek logo/ building but would love some designs with and without it.
WE ARE LOOKING FOR A ROUND LABEL. The pictures provided below are of the old bottle.
There is a picture of the ringneck bottle below. The size of the label is 4.00 x 7.00.

```html
<!DOCTYPE html>
<html lang="en">
<head>
<meta charset="utf-8">
<title>Marlowe's Classic Dressing – Label</title>
<link href="https://fonts.googleapis.com/css2?family=Josefin+Sans:wght@300;400;600&family=Lobster&display=swap" rel="stylesheet">
<style>
  :root {
    --label-blue: #1b5fa8;
    --label-blue-deep: #134a8a;
    --label-white: #ffffff;
    --backdrop-light: #fbfbfb;
    --backdrop-dark: #e4e4e4;
  }
  html, body {
    margin: 0;
    width: 1200px;
    height: 791px;
    overflow: hidden;
  }
  body {
    background: radial-gradient(ellipse at 50% 20%, var(--backdrop-light) 0%, var(--backdrop-dark) 100%);
  }
  .label-art {
    display: block;
    width: 1200px;
    height: 791px;
  }
  .label-outer { fill: var(--label-white); filter: drop-shadow(0 18px 22px rgba(0,0,0,0.22)); }
  .brand-name {
    font-family: "Josefin Sans", sans-serif;
    font-weight: 600;
    font-size: 30px;
    fill: var(--label-white);
  }
  .product-name {
    font-family: "Josefin Sans", sans-serif;
    font-weight: 400;
    font-size: 60px;
    letter-spacing: 1px;
    fill: var(--label-white);
  }
  .product-type {
    font-family: "Josefin Sans", sans-serif;
    font-weight: 400;
    font-size: 14px;
    letter-spacing: 4.5px;
    fill: var(--label-white);
  }
  .ribbon-text {
    font-family: "Lobster", cursive;
    font-size: 15px;
    fill: var(--label-blue);
  }
  .small-print {
    font-family: "Josefin Sans", sans-serif;
    font-size: 11px;
    fill: var(--label-white);
  }
  .badge-text {
    font-family: "Josefin Sans", sans-serif;
    font-size: 8px;
    fill: var(--label-white);
  }
</style>
</head>
<body>
<svg class="label-art" viewBox="0 0 1200 791" xmlns="http://www.w3.org/2000/svg">
  <defs>
    <radialGradient id="label-field" cx="50%" cy="50%" r="60%">
      <stop offset="0%" stop-color="#1b5fa8"/>
      <stop offset="100%" stop-color="#134a8a"/>
    </radialGradient>
    <clipPath id="label-inner-clip">
      <ellipse cx="600" cy="395" rx="131" ry="236"/>
    </clipPath>
  </defs>

  <ellipse class="label-outer" cx="600" cy="395" rx="143" ry="250"/>
  <ellipse cx="600" cy="395" rx="131" ry="236" fill="url(#label-field)"/>

  <g clip-path="url(#label-inner-clip)">
    <rect x="571" y="171" width="59" height="448" fill="var(--label-white)" opacity="0.92" role="img" aria-label="Classical Greek column running vertically through the label"/>
    <rect x="460" y="307" width="280" height="147" fill="var(--label-blue)"/>
    <line x1="460" y1="309" x2="740" y2="309" stroke="var(--label-white)" stroke-width="1"/>
    <line x1="460" y1="452" x2="740" y2="452" stroke="var(--label-white)" stroke-width="1"/>
  </g>

  <text class="brand-name" x="600" y="350" text-anchor="middle">Marlowe's</text>
  <text class="product-name" x="600" y="420" text-anchor="middle">GREEK</text>
  <text class="product-type" x="602" y="443" text-anchor="middle">DRESSING</text>

  <polygon points="498,467 702,467 694,478.5 702,490 498,490 506,478.5" fill="var(--label-white)"/>
  <text class="ribbon-text" x="600" y="484" text-anchor="middle">Original Recipe From 1957</text>

  <circle cx="545" cy="557" r="19" fill="none" stroke="var(--label-white)" stroke-width="1.5"/>
  <text class="badge-text" x="545" y="555" text-anchor="middle">GLUTEN</text>
  <text class="badge-text" x="545" y="564" text-anchor="middle">FREE</text>

  <text class="small-print" x="657" y="555" text-anchor="middle">8 FL. OZ.</text>
  <text class="small-print" x="657" y="569" text-anchor="middle">(237ml)</text>
</svg>
</body>
</html>
```